Lumora Works - Design & Marketing Website Re-branding

UPDATE:
We are working on finalizing our color palette but are hoping that the designers will guide us to the right choice of colors by looking at our color inspiration file that we just uploaded and lead us in the right direction.

-----

I am exploring new design inspiration for a re-branding of my website. My current website is old and outdated and I lack the time to design it myself in addition to the fact that I am my own worst client.

I do website design, development and marketing as well as some SEO consulting and business development for small to mid-size companies in a range of industries.

https://lumoraworks.example

I like clean modern designs without cartoon images. The brands I'm going after are looking for a professional look and feel. I need something that shows my many years of being in business that is very professional.

I prefer minimal use of color. Mostly black and white with maybe one or two other colors. I am open to the suggestions by the designer.

Target Market(s)

Small to mid-size companies

Industry/Entity Type

Website Design, SEO and Markeitng

Number of Pages Required

4 page

Font styles to use
Sans Serif

Requirements
Must have
• Must be clean, modern and professional - I am not a huge fan of a lot of color and I'm open to new color suggestions by the designer
Nice to have
• A good balance of whitespace to content and graphics
Should not have
• Please no people illustrations

```html
<!DOCTYPE html>
<html lang="en">
<head>
<meta charset="utf-8">
<title>Lumora Works — Design &amp; Marketing</title>
<link href="https://fonts.googleapis.com/css2?family=Archivo:wght@700;800;900&family=Montserrat:wght@400;500;600;700&family=Source+Sans+3:wght@400;600&family=Arimo:wght@400;700&display=swap" rel="stylesheet">
<style>
:root{
  --red:#e8194a;
  --dark:#323232;
  --side:#121212;
  --white:#ffffff;
  --paper:#efefef;
  --ink:#1b1b1b;
  --mute:#555555;
  --ghost:#d3caca;
  --rule:#e4e4e4;
  --navy:#2e2f6b;
}
*{margin:0;padding:0;box-sizing:border-box}
html,body{width:1200px;height:4563px;overflow:hidden}
body{position:relative;background:var(--dark);font-family:"Source Sans 3",sans-serif;color:var(--ink)}
.abs{position:absolute}
.sidebar{left:0;top:0;width:112px;height:4563px;background:var(--side);z-index:5}
.side-brand{left:14px;top:22px;width:86px;color:var(--white);font-family:"Montserrat",sans-serif;font-weight:700;font-size:15px;line-height:18px}
.side-line{left:55px;width:1px;height:40px;background:#777}
.side-social{left:49px;width:13px}
.side-social span{display:block;width:13px;height:13px;border-radius:50%;background:var(--red);margin-bottom:9px}
.header-brand{left:129px;top:26px;color:var(--white);font-family:"Montserrat",sans-serif;font-weight:600;font-size:23px;z-index:3}
.nav{left:470px;top:34px;display:flex;gap:0;z-index:3}
.nav a{color:var(--white);text-decoration:none;font-family:"Montserrat",sans-serif;font-size:11px;position:absolute;white-space:nowrap}
.btn{position:absolute;background:var(--red);color:var(--white);font-family:"Montserrat",sans-serif;font-weight:700;font-size:10.5px;letter-spacing:.3px;display:flex;align-items:center;justify-content:center;gap:10px;text-transform:uppercase}
.btn svg{width:22px;height:8px}
.hero{left:112px;top:0;width:1088px;height:638px;background:linear-gradient(90deg,#1c1c1e 0%,#2a2b30 35%,#4d5560 60%,#3c4350 100%)}
.hero-kicker{left:353px;top:153px;color:var(--white);font-size:11px;font-family:"Montserrat",sans-serif}
.hero-kicker-line{left:307px;top:161px;width:42px;height:1px;background:var(--red)}
.hero-title{left:200px;top:182px;color:var(--white);font-family:"Archivo",sans-serif;font-weight:800;font-size:55px;line-height:63px;width:460px}
.hero-sub{left:202px;top:385px;color:var(--white);font-size:15px}
.big-head{position:absolute;left:200px;font-family:"Archivo",sans-serif;font-weight:800;font-size:78px;line-height:1;white-space:nowrap;z-index:2}
.big-head .fill{color:var(--ghost)}
.big-head .line{color:transparent;-webkit-text-stroke:1.6px var(--ghost)}
.big-head .dot{color:var(--red)}
.panel{position:absolute;left:112px;width:1088px}
.panel.white{background:var(--white)}
.panel.paper{background:var(--paper)}
.vrule{position:absolute;top:0;width:1px;height:100%;background:var(--rule)}
.service{position:absolute;top:62px;width:230px}
.service svg.ico{width:38px;height:38px;display:block}
.service h3{font-family:"Montserrat",sans-serif;font-weight:700;font-size:17px;margin-top:28px;color:var(--ink)}
.service p{font-size:10px;line-height:19.5px;color:var(--mute);margin-top:6px}
.service .arrow{position:absolute;top:232px;left:0;width:30px;height:10px}
.num{position:absolute;top:340px;font-family:"Archivo",sans-serif;font-weight:700;font-size:84px;line-height:100px;color:transparent;-webkit-text-stroke:1.2px #cfcfd8}
.tab{position:absolute;top:50px;font-size:12px;font-family:"Montserrat",sans-serif}
.tab-line{position:absolute;top:57px;height:1px}
.sec-title{position:absolute;font-family:"Montserrat",sans-serif;font-weight:600;font-size:18px;color:var(--ink)}
.sec-desc{position:absolute;font-size:11px;color:var(--mute)}
.shot{position:absolute;top:200px;height:261px}
.cap{position:absolute;top:480px;display:flex;align-items:baseline;gap:10px;font-size:9px;color:#777;white-space:nowrap}
.cap b{font-family:"Montserrat",sans-serif;font-weight:700;font-size:13.5px;color:var(--ink)}
.about-copy{position:absolute;left:0;top:0;width:714px;height:482px;background:linear-gradient(90deg,#ebebea,#d9d9d8)}
.about-photo{position:absolute;left:714px;top:0;width:374px;height:482px;background:linear-gradient(180deg,#cfcfcf 0%,#8d8d8d 45%,#4a4a4a 100%)}
.about-title{left:92px;top:52px;font-family:"Archivo",sans-serif;font-weight:800;font-size:60px;color:#222}
.about-p{left:92px;width:380px;font-size:10px;line-height:19.5px;color:#444}
.about-ghost{left:92px;top:362px;font-family:"Archivo",sans-serif;font-weight:700;font-size:88px;line-height:1;color:transparent;-webkit-text-stroke:1.4px #c9c9c9;white-space:nowrap}
.quote-photo{left:90px;top:54px;width:324px;height:359px;background:linear-gradient(180deg,#a9a9a6 0%,#8f8e8a 60%,#6d6660 100%)}
.quote{left:476px;width:400px;font-family:"Arimo",sans-serif;font-size:14.5px;line-height:23.5px;color:#555}
.res-card{position:absolute;top:64px;width:346px}
.res-img{width:346px;height:200px}
.res-card h4{font-family:"Montserrat",sans-serif;font-weight:600;font-size:16px;line-height:22px;margin-top:20px;color:var(--ink)}
.res-card p{font-size:10px;line-height:17px;color:#666;margin-top:8px}
.res-card .under{height:1px;background:#8b8fb3;margin-top:10px}
.contact{left:112px;top:3853px;width:1088px;height:511px;background:var(--red)}
.field{position:absolute;border:1px solid rgba(255,255,255,.7);color:var(--white);font-size:11px;padding:10px 14px}
.footer-brand{left:270px;top:4436px;color:var(--white);font-family:"Montserrat",sans-serif;font-weight:600;font-size:23px}
.footer-mark{left:208px;top:4429px;width:48px;height:48px;border-radius:50%;background:var(--white)}
.small-white{color:var(--white);font-size:9px}
</style>
</head>
<body>

<!-- Sidebar -->
<aside class="abs sidebar">
  <div class="abs side-brand">Lumora<br>Works</div>
  <div class="abs side-line" style="top:155px"></div>
  <div class="abs side-social" style="top:484px"><span></span><span></span><span></span></div>
  <div class="abs side-line" style="top:780px"></div>
  <div class="abs side-social" style="top:1066px"><span></span><span></span><span></span></div>
  <div class="abs side-line" style="top:1420px"></div>
  <div class="abs side-social" style="top:1672px"><span></span><span></span><span></span></div>
  <div class="abs side-line" style="top:2120px"></div>
  <div class="abs side-social" style="top:2398px"><span></span><span></span><span></span></div>
  <div class="abs side-line" style="top:2960px"></div>
  <div class="abs side-social" style="top:3107px"><span></span><span></span><span></span></div>
  <div class="abs side-line" style="top:3700px"></div>
  <div class="abs side-social" style="top:3788px"><span></span><span></span><span></span></div>
  <div class="abs side-line" style="top:4290px"></div>
  <div class="abs side-social" style="top:4337px"><span></span><span></span><span></span></div>
</aside>

<!-- Hero -->
<section>
  <div class="abs hero" role="img" aria-label="Photo of two smiling colleagues working together at a laptop in a dim office"></div>
  <div class="abs header-brand">Lumora Works</div>
  <nav class="abs nav">
    <a style="left:0">Simplify</a><a style="left:78px">Design</a><a style="left:151px">Care</a><a style="left:213px">Inspire</a><a style="left:286px">About</a><a style="left:355px">Collaborate</a><a style="left:451px">Connect</a>
  </nav>
  <div class="btn" style="left:996px;top:25px;width:152px;height:33px;font-weight:500;font-size:10px">Request a call <svg viewBox="0 0 22 8"><path d="M0 4h20M16 1l4 3-4 3" fill="none" stroke="#fff" stroke-width="1.2"/></svg></div>
  <div class="abs hero-kicker-line"></div>
  <div class="abs hero-kicker">Welcome to your Lumora Works</div>
  <h1 class="abs hero-title">Every business has a story. We help you tell it</h1>
  <p class="abs hero-sub">Compelling website experiences that elevate your business.</p>
  <div class="btn" style="left:204px;top:429px;width:143px;height:37px">What we do <svg viewBox="0 0 22 8"><path d="M0 4h20M16 1l4 3-4 3" fill="none" stroke="#fff" stroke-width="1.2"/></svg></div>
  <h2 class="big-head" style="top:565px"><span class="fill">Discover</span> <span class="line">Our Services</span><span class="dot">.</span></h2>
</section>

<!-- Services -->
<section class="panel white" style="top:638px;height:438px">
  <div class="vrule" style="left:331px"></div>
  <div class="vrule" style="left:576px"></div>
  <div class="vrule" style="left:833px"></div>
  <div class="vrule" style="left:1052px"></div>

  <div class="service" style="left:90px">
    <svg class="ico" viewBox="0 0 38 38"><rect x="2" y="8" width="28" height="20" rx="2" fill="#555"/><rect x="12" y="28" width="8" height="5" fill="#555"/><rect x="8" y="33" width="16" height="2" fill="#555"/><path d="M22 20L35 5l2 2-13 15z" fill="var(--red)"/></svg>
    <h3>Website Design</h3>
    <p>Web design involves creating the visual elements and layout of a website, while coding involves translating these designs into a functional website using programming languages like HTML, CSS, and JavaScript. Typically, dedicated web developers translate the designs to code.</p>
    <svg class="arrow" viewBox="0 0 30 10"><path d="M0 5h28M23 1l5 4-5 4" fill="none" stroke="var(--red)" stroke-width="1.3"/></svg>
  </div>
  <div class="service" style="left:333px">
    <svg class="ico" viewBox="0 0 38 38"><circle cx="17" cy="17" r="14" fill="none" stroke="#555" stroke-width="3"/><ellipse cx="17" cy="17" rx="6" ry="14" fill="none" stroke="#555" stroke-width="2"/><path d="M3 17h28M6 9h22M6 25h22" stroke="#555" stroke-width="2"/><path d="M22 22l12 5-5 2-2 5z" fill="var(--red)"/></svg>
    <h3>Website Development</h3>
    <p>Web development is the work involved in developing a website for the Internet (World Wide Web) or an intranet (a private network). Web development can range from developing a simple single static page of plain text to complex web applications, electronic businesses, and social network services.</p>
    <svg class="arrow" viewBox="0 0 30 10"><path d="M0 5h28M23 1l5 4-5 4" fill="none" stroke="var(--red)" stroke-width="1.3"/></svg>
  </div>
  <div class="service" style="left:579px">
    <svg class="ico" viewBox="0 0 38 38"><rect x="3" y="8" width="32" height="22" rx="2" fill="#555"/><circle cx="16" cy="18" r="5" fill="none" stroke="#fff" stroke-width="2"/><path d="M20 22l5 5" stroke="#fff" stroke-width="2"/><rect x="26" y="3" width="10" height="7" fill="var(--red)"/><rect x="10" y="32" width="18" height="2" fill="#555"/></svg>
    <h3>SEO consulting</h3>
    <p>Explore what an SEO consultant can contribute to your business and how to hire the right one for your business goals. Featured Image): A male wearing a yellow jacket, is sitting at his desk working on a laptop computer performing his duties as an SEO consultant.</p>
    <svg class="arrow" viewBox="0 0 30 10"><path d="M0 5h28M23 1l5 4-5 4" fill="none" stroke="var(--red)" stroke-width="1.3"/></svg>
  </div>
  <div class="service" style="left:834px;width:210px">
    <svg class="ico" viewBox="0 0 38 38"><circle cx="18" cy="20" r="11" fill="none" stroke="#555" stroke-width="6" stroke-dasharray="5 3"/><circle cx="18" cy="20" r="4" fill="#555"/><path d="M20 18L34 4l2 2-14 14z" fill="var(--red)"/></svg>
    <h3>Business Development</h3>
    <p>Business development is the creation of long-term value for an organization from customers, markets, and relationships.</p>
    <svg class="arrow" viewBox="0 0 30 10"><path d="M0 5h28M23 1l5 4-5 4" fill="none" stroke="var(--red)" stroke-width="1.3"/></svg>
  </div>
  <div class="btn" style="left:864px;top:319px;width:185px;height:37px">View all services <svg viewBox="0 0 22 8"><path d="M0 4h20M16 1l4 3-4 3" fill="none" stroke="#fff" stroke-width="1.2"/></svg></div>
  <div class="num" style="left:88px">01</div>
  <div class="num" style="left:331px">02</div>
  <div class="num" style="left:577px">03</div>
  <div class="num" style="left:832px">04</div>
</section>

<h2 class="big-head" style="top:1204px"><span class="fill">Explore</span> <span class="line">Our Work</span><span class="dot">.</span></h2>

<!-- Work -->
<section class="panel white" style="top:1276px;height:550px">
  <div class="tab-line" style="left:90px;width:145px;background:var(--red)"></div>
  <div class="tab" style="left:241px;color:var(--red)">Website Design</div>
  <div class="tab-line" style="left:349px;width:147px;background:#7c7fa6"></div>
  <div class="tab" style="left:500px;color:var(--navy)">Website Development</div>
  <div class="sec-title" style="left:90px;top:119px">Website Design</div>
  <div class="sec-desc" style="left:90px;top:150px">Outstanding website design can help you make a lasting impression. Get modern web design done by the top website designers.</div>
  <div class="btn" style="left:864px;top:117px;width:185px;height:37px">View all projects <svg viewBox="0 0 22 8"><path d="M0 4h20M16 1l4 3-4 3" fill="none" stroke="#fff" stroke-width="1.2"/></svg></div>

  <div class="shot" role="img" aria-label="B2B website design mockup pages in lavender and white" style="left:90px;width:347px;background:linear-gradient(90deg,#b6b3ee,#e8e6f7 55%,#c9c6f1)"></div>
  <div class="shot" role="img" aria-label="Landing page design mockup in light grey tones" style="left:451px;width:347px;background:linear-gradient(90deg,#c3c8d4,#eef0f4 55%,#cfd4dd)"></div>
  <div class="shot" role="img" aria-label="Landing page design shown on a desktop monitor with a dark space theme" style="left:813px;width:217px;background:linear-gradient(180deg,#f4f4f4 0%,#1d2740 20%,#2a3556 70%,#e6e6e6 100%)"></div>

  <div class="cap" style="left:90px"><b>B2B Website Design</b> <span>♡ Like(24)</span><span>◉ View(405)</span><span>⋖ Share(08)</span></div>
  <div class="cap" style="left:451px"><b>Landing Page Design</b> <span>♡ Like(24)</span><span>◉ View(405)</span><span>⋖ Share(08)</span></div>
  <div class="cap" style="left:813px"><b>Landing Page Design</b> <span>♡ Like(24)</span></div>
</section>

<h2 class="big-head" style="top:1957px"><span class="fill">Who</span> <span class="line">We Are</span><span class="dot">.</span></h2>

<!-- About -->
<section class="panel" style="top:2026px;height:482px">
  <div class="about-copy"></div>
  <div class="about-photo" role="img" aria-label="Modern open-plan office interior with desks, chairs and large windows"></div>
  <svg class="abs" style="left:1000px;top:26px" width="26" height="10" viewBox="0 0 26 10"><path d="M0 5h24M19 1l5 4-5 4" fill="none" stroke="#fff" stroke-width="1.3"/></svg>
  <h2 class="abs about-title">About us</h2>
  <p class="abs about-p" style="top:122px">We are a collaborative team of word nerds, choreographers of shapes &amp; ideas, ambassadors of data, content warriors and inspirational conversationalists ready to help you no matter where you are in your journey.</p>
  <p class="abs about-p" style="top:200px">We have a deep understanding of what it takes to grow a business and we collaborate with you every step of the way from strategy to implementation.</p>
  <div class="btn" style="left:90px;top:259px;width:184px;height:36px">Learn more story <svg viewBox="0 0 22 8"><path d="M0 4h20M16 1l4 3-4 3" fill="none" stroke="#fff" stroke-width="1.2"/></svg></div>
  <div class="abs about-ghost">Lumora Works</div>
</section>

<h2 class="big-head" style="top:2636px"><span class="fill">Client</span> <span class="line">Testimonials</span><span class="dot">.</span></h2>

<!-- Testimonials -->
<section class="panel white" style="top:2706px;height:466px">
  <div class="abs quote-photo" role="img" aria-label="People standing against a wall using phones, with floating communication icons"></div>
  <div class="abs" style="left:476px;top:92px;color:#f2b300;font-size:16px;letter-spacing:1px">★★★★★</div>
  <div class="abs" style="left:476px;top:126px;color:var(--red);font-family:'Arimo',sans-serif;font-weight:700;font-size:17px">Highly Recommend!</div>
  <p class="abs quote" style="top:158px">Lorem Ipsum is simply dummy text of the printing and typesetting industry. Lorem Ipsum has been the industry's standard dummy text ever since the 1500s, when an unknown printer took a galley of type and scrambled it to make a type specimen book.</p>
  <p class="abs quote" style="top:300px">and more recently with desktop publishing software like Quillset Pro including versions of Lorem Ipsum.</p>
  <div class="abs" style="left:476px;top:358px;color:var(--red);font-family:'Arimo',sans-serif;font-weight:700;font-size:15px">Nora Weller, <span style="font-size:10px">Chief Orienter</span></div>
  <svg class="abs" style="left:884px;top:134px" width="154" height="176" viewBox="0 0 154 176"><polygon points="0,18 52,18 52,0 90,38 52,76 52,58 0,58" fill="#d6d6d6"/><polygon points="154,118 102,118 102,98 64,137 102,176 102,158 154,158" fill="#d6d6d6"/></svg>
  <div class="btn" style="left:882px;top:376px;width:167px;height:36px;font-weight:500">View testimonials <svg viewBox="0 0 22 8"><path d="M0 4h20M16 1l4 3-4 3" fill="none" stroke="#fff" stroke-width="1.2"/></svg></div>
</section>

<h2 class="big-head" style="top:3304px"><span class="fill">Company</span> <span class="line">Resources</span><span class="dot">.</span></h2>

<!-- Resources -->
<section class="panel paper" style="top:3373px;height:480px">
  <article class="res-card" style="left:90px">
    <div class="res-img" role="img" aria-label="Illustration of search optimisation concepts around a laptop" style="background:linear-gradient(135deg,#d9dde2,#8e9aa6 60%,#5b6670)"></div>
    <h4>Searchly Algorithm Updates of 2024 – Impacts and Solutions</h4>
    <p>Searchly keeps on improving its algorithm for the improvement of...</p>
    <div class="under"></div>
  </article>
  <article class="res-card" style="left:476px">
    <div class="res-img" role="img" aria-label="Hands typing on a laptop showing a blog page" style="background:linear-gradient(135deg,#3a4a66,#8aa0c0 55%,#d8d2c8)"></div>
    <h4>Rules to follow for SEO Content Writing</h4>
    <p>In any strategy of digital marketing, getting organic traffic is Lorem Ipsum is simply dummy text of the printing and typesetting industry.</p>
    <div class="under"></div>
  </article>
  <div class="abs" style="left:996px;top:245px;width:13px;height:13px;border-radius:50%;background:var(--red)"></div>
  <div class="btn" style="left:882px;top:388px;width:167px;height:37px;font-weight:500">View all resources <svg viewBox="0 0 22 8"><path d="M0 4h20M16 1l4 3-4 3" fill="none" stroke="#fff" stroke-width="1.2"/></svg></div>
</section>

<!-- Contact -->
<section class="abs contact">
  <div class="abs" style="left:90px;top:97px;width:145px;height:1px;background:#fff"></div>
  <div class="abs small-white" style="left:241px;top:90px;font-size:10px">Lumora Works Contact Us</div>
  <h2 class="abs" style="left:90px;top:112px;color:#fff;font-family:'Archivo',sans-serif;font-weight:800;font-size:60px">Connect with us<span>.</span></h2>
  <p class="abs" style="left:92px;top:191px;color:#fff;font-size:14px">Let's have a conversation to discuss your needs and how we can help.</p>
  <div class="field" style="left:90px;top:224px;width:298px;height:39px">Name</div>
  <div class="field" style="left:397px;top:224px;width:296px;height:39px">Email</div>
  <div class="field" style="left:702px;top:224px;width:297px;height:39px">Phone</div>
  <div class="field" style="left:90px;top:273px;width:909px;height:83px">Message</div>
  <div class="btn" style="left:90px;top:380px;width:138px;height:37px;background:#fff;color:var(--red);font-weight:500">Send message <svg viewBox="0 0 22 8"><path d="M0 4h20M16 1l4 3-4 3" fill="none" stroke="var(--red)" stroke-width="1.2"/></svg></div>
</section>
<h2 class="big-head" style="top:4290px"><span class="fill">Lumora</span> <span class="line">Works</span><span class="dot" style="color:#fff">.</span></h2>

<!-- Footer -->
<footer>
  <div class="abs footer-mark"></div>
  <div class="abs footer-brand">Lumora Works</div>
  <div class="abs small-white" style="left:202px;top:4516px">© 2024 Lumora Works LLC. All Rights Reserved.</div>
  <div class="abs small-white" style="left:202px;top:4531px">Privacy &nbsp;|&nbsp; Terms &nbsp;|&nbsp; Disclaimer</div>
  <div class="abs" style="left:728px;top:4436px;color:#fff;font-family:'Montserrat',sans-serif;font-weight:600;font-size:16px">Keep Upto Date</div>
  <div class="abs small-white" style="left:728px;top:4473px">Enter your email below and get monthly update right into your inbox!</div>
  <div class="abs small-white" style="left:730px;top:4516px;font-size:11px">Enter email</div>
  <div class="abs" style="left:728px;top:4537px;width:288px;height:1px;background:#aaa"></div>
  <div class="btn" style="left:1016px;top:4502px;width:60px;height:41px"><svg viewBox="0 0 22 8"><path d="M0 4h20M16 1l4 3-4 3" fill="none" stroke="#fff" stroke-width="1.2"/></svg></div>
</footer>

</body>
</html>
```